Harbor Vantage Web Design Project

We need a website design for a start up company called "Harbor Vantage". We provide business consultancy services as well as technology-related services (IT). The design should communicate simplicity and elegance. The domain name of the site will be harborvantage-example.com. The logo of the company is https://files.example-share.net/u/7418205/4630_2116587_67315_image.jpg

Target Market(s)

SMB, Corporates, Semi-governments, Governments.

Industry/Entity Type

Business

Requirements
Must have
• - The background of the pages should be white or soft grey, but we are open for suggestions.
- The pages should have nice menu animations.
- The pages should be "portal-style", with multiple placeholders for different sections and multiple tabs.
Nice to have
• The page should auto-fit the screen and scroll vertically as much as needed.
Should not have
• - Flash Animations.
- Generic Photos.

```html
<!DOCTYPE html>
<html lang="en">
<head>
<meta charset="utf-8">
<title>Harbor Vantage</title>
<link href="https://fonts.googleapis.com/css2?family=Exo+2:ital,wght@0,300;0,400;0,500&family=Lato:ital,wght@0,400;0,700;1,400&display=swap" rel="stylesheet">
<style>
:root{
  --red:#d0021b;
  --blue:#1d62b3;
  --text:#4a4a4a;
  --muted:#6b6b6b;
  --line:#dcdcdc;
  --foot:#f6f6f6;
}
*{margin:0;padding:0;box-sizing:border-box}
html,body{width:1006px;height:1200px;overflow:hidden;background:#fff}
body{position:relative;font-family:"Lato",sans-serif;color:var(--text)}
.abs{position:absolute}
.top-rule{left:0;top:0;width:1006px;height:3px;background:var(--red)}
.brand{left:61px;top:44px;display:flex;align-items:center;gap:8px;font-family:"Exo 2",sans-serif;font-weight:500;font-size:22px;color:var(--blue);white-space:nowrap}
.brand-dot{width:22px;height:22px;border-radius:50%;background:var(--red)}
.nav a{position:absolute;top:70px;font-family:"Exo 2",sans-serif;font-size:12px;color:var(--red);text-decoration:none;letter-spacing:.2px}
.nav a.active{font-weight:500;padding-bottom:5px;border-bottom:2px solid var(--red)}
.hero{left:57px;top:116px;width:891px;height:369px;border-radius:6px;background:linear-gradient(#f4f4f4,#ececec);box-shadow:0 6px 10px -6px rgba(0,0,0,.25)}
.hero-photo{left:483px;top:139px;width:444px;height:309px;border-radius:4px;background:radial-gradient(ellipse at 50% 50%,#3a4b7a 0 28%,#c9cdd3 40%,#ececec 70%)}
.hero-title{left:95px;top:170px;z-index:2;font-family:"Exo 2",sans-serif;font-weight:300;font-size:20px;color:var(--blue);white-space:nowrap}
.hero-sub{left:94px;top:200px;z-index:2;font-family:"Exo 2",sans-serif;font-size:14px;color:var(--red);white-space:nowrap}
.hero-intro{left:96px;top:227px;z-index:2;font-size:10.2px;line-height:17.5px;width:318px}
.checks{left:98px;top:270px;z-index:2;list-style:none;font-size:10.2px;line-height:19.2px}
.checks li{display:flex;align-items:center;gap:8px}
.quote-btn{left:98px;top:384px;width:118px;height:35px;background:var(--red);color:#fff;font-family:"Exo 2",sans-serif;font-size:15px;display:flex;align-items:center;justify-content:center;text-decoration:none}
.slider-tab{left:458px;top:459px;width:90px;height:26px}
.lead{left:100px;top:517px;width:806px;text-align:center;font-style:italic;font-size:13px;line-height:22px;color:var(--muted)}
.hr{left:54px;top:581px;width:893px;height:1px;background:var(--line)}
.card{position:absolute;top:605px;width:203px}
.card .thumb{height:110px;border:1px solid #ddd;border-radius:4px}
.card h3{margin:16px 0 0 5px;font-family:"Exo 2",sans-serif;font-weight:400;font-size:15px;color:var(--blue)}
.card .tag{margin:3px 0 0 5px;font-size:10px;line-height:15.5px;font-weight:700;color:var(--red)}
.card .desc{margin:2px 0 0 5px;width:192px;font-size:10px;line-height:15.7px;color:var(--muted)}
.card .more{display:inline-flex;align-items:center;gap:5px;margin:16px 0 0 5px;font-family:"Exo 2",sans-serif;font-size:12px;color:var(--red);text-decoration:none}
.footer-area{left:0;top:892px;width:1006px;height:262px;background:var(--foot);border-top:3px solid #e2e2e2}
.vline{top:896px;width:1px;height:196px;background:var(--line)}
.foot-h{font-family:"Exo 2",sans-serif;font-weight:400;font-size:15.5px;color:#444;white-space:nowrap}
.social{left:53px;top:953px;display:flex;gap:5px}
.social span{width:23px;height:23px;border-radius:50%;background:#8a8a8a}
.blog{left:208px;top:944px;width:265px;font-size:9.6px;line-height:15.6px}
.blog p{font-style:italic}
.blog .by{font-style:normal;font-weight:700;font-size:10.4px;margin:5px 0 9px}
.svc{left:509px;top:944px;list-style:none;font-size:9.8px;line-height:20.9px}
.svc li{display:flex;align-items:center;gap:8px}
.news{left:741px;top:946px;font-size:9.8px;line-height:14px}
.news p{margin-bottom:6.5px}
.bottom-bar{left:0;top:1154px;width:1006px;height:46px;background:var(--red);color:#fff;font-size:10px;font-weight:700}
.bottom-bar .copy{position:absolute;left:57px;top:9px}
.bottom-bar .links{position:absolute;right:63px;top:9px;word-spacing:1px}
</style>
</head>
<body>
<div class="abs top-rule"></div>

<header>
  <div class="abs brand"><span class="brand-dot"></span>Harbor Vantage</div>
  <nav class="nav">
    <a class="active" href="#" style="left:432px">MAIN</a>
    <a href="#" style="left:497px">ABOUT</a>
    <a href="#" style="left:566px">SERVICES</a>
    <a href="#" style="left:647px">PORTFOLIO</a>
    <a href="#" style="left:740px">SUPPORT</a>
    <a href="#" style="left:821px">BLOG</a>
    <a href="#" style="left:884px">CONTACT</a>
  </nav>
</header>

<section>
  <div class="abs hero"></div>
  <div class="abs hero-photo" role="img" aria-label="Two business people leaning on a large laptop showing an online store"></div>
  <h1 class="abs hero-title">We Provide E-Commerce Portal &amp; Services</h1>
  <div class="abs hero-sub">Lorem ipsum dolor sit amet, consectetuer elit.</div>
  <p class="abs hero-intro">Lorem ipsum dolor sit amet, consectetuer adipiscing elit. Nam cursus. Morbi ut mi. Nullam enim leo, egestas id, condimentum at.</p>
  <ul class="abs checks">
    <li><svg width="11" height="10" viewBox="0 0 11 10"><path d="M1 5l3 3 6-7" fill="none" stroke="#d0021b" stroke-width="2"/></svg>Proin dui lectus cursus eu mattis laoreet</li>
    <li><svg width="11" height="10" viewBox="0 0 11 10"><path d="M1 5l3 3 6-7" fill="none" stroke="#d0021b" stroke-width="2"/></svg>Viverra sit amet quam.</li>
    <li><svg width="11" height="10" viewBox="0 0 11 10"><path d="M1 5l3 3 6-7" fill="none" stroke="#d0021b" stroke-width="2"/></svg>Curabitur vel dolor ultrices ipsum tristique.</li>
    <li><svg width="11" height="10" viewBox="0 0 11 10"><path d="M1 5l3 3 6-7" fill="none" stroke="#d0021b" stroke-width="2"/></svg>Praesent vitae lacus.</li>
    <li><svg width="11" height="10" viewBox="0 0 11 10"><path d="M1 5l3 3 6-7" fill="none" stroke="#d0021b" stroke-width="2"/></svg>Ut velit enim vestibulum non</li>
  </ul>
  <a class="abs quote-btn" href="#">Get a Quote</a>
  <svg class="abs slider-tab" viewBox="0 0 90 26" aria-hidden="true">
    <path d="M0 26 C14 26 12 0 26 0 H64 C78 0 76 26 90 26Z" fill="#d4d4d4"/>
    <circle cx="25" cy="14" r="4" fill="#444"/><circle cx="38" cy="14" r="4" fill="#fff"/>
    <circle cx="51" cy="14" r="4" fill="#fff"/><circle cx="64" cy="14" r="4" fill="#fff"/>
  </svg>
</section>

<p class="abs lead">Lorem ipsum dolor sit amet, consectetuer adipiscing elit. Nam cursus. Morbi ut mi. Nullam enim leo, egestas id, condimentum at, laoreet mattis, massa. Sed eleifend nonummy diam. Praesent mauris ante, elementum et, bibendum at, posuere sit amet, nibh.</p>
<div class="abs hr"></div>

<section>
  <article class="card" style="left:57px">
    <div class="thumb" role="img" aria-label="Colourful speech bubbles with question marks" style="background:linear-gradient(120deg,#f7a15a,#e93f8a 45%,#5cc6c4)"></div>
    <h3>Featured Service</h3>
    <p class="tag">Lorem ipsum dolor sit amet, consec<br>tetuer adipiscing elit.</p>
    <p class="desc">Nam cursus. Morbi ut mi. Nullam enim leo, egestas id, condimentum at, laoreet<br>mattis, massa.</p>
    <a class="more" href="#">learn more <svg width="5" height="8"><path d="M0 0l5 4-5 4z" fill="#d0021b"/></svg></a>
  </article>
  <article class="card" style="left:284px">
    <div class="thumb" role="img" aria-label="Figures with shopping carts around a large orange at sign" style="background:radial-gradient(circle,#f29a1f 0 25%,#f6f6f6 55%)"></div>
    <h3>Featured Service</h3>
    <p class="tag">Lorem ipsum dolor sit amet, consec<br>tetuer adipiscing elit.</p>
    <p class="desc">Nam cursus. Morbi ut mi. Nullam enim leo, egestas id, condimentum at, laoreet<br>mattis, massa.</p>
    <a class="more" href="#">learn more <svg width="5" height="8"><path d="M0 0l5 4-5 4z" fill="#d0021b"/></svg></a>
  </article>
  <article class="card" style="left:514px">
    <div class="thumb" role="img" aria-label="Online shopping illustration with bags, cart and gift card" style="background:linear-gradient(#cfe6f7,#eef6fc);border-color:#cfe6f7"></div>
    <h3>Featured Service</h3>
    <p class="tag">Lorem ipsum dolor sit amet, consec<br>tetuer adipiscing elit.</p>
    <p class="desc">Nam cursus. Morbi ut mi. Nullam enim leo, egestas id, condimentum at, laoreet<br>mattis, massa.</p>
    <a class="more" href="#">learn more <svg width="5" height="8"><path d="M0 0l5 4-5 4z" fill="#d0021b"/></svg></a>
  </article>
  <article class="card" style="left:742px">
    <div class="thumb" role="img" aria-label="Devices connected around a blue shopping cart" style="background:radial-gradient(circle,#7fd0ee 0 12%,#f4f6f8 45%)"></div>
    <h3>Featured Service</h3>
    <p class="tag">Lorem ipsum dolor sit amet, consec<br>tetuer adipiscing elit.</p>
    <p class="desc">Nam cursus. Morbi ut mi. Nullam enim leo, egestas id, condimentum at, laoreet<br>mattis, massa.</p>
    <a class="more" href="#">learn more <svg width="5" height="8"><path d="M0 0l5 4-5 4z" fill="#d0021b"/></svg></a>
  </article>
</section>

<footer>
  <div class="abs footer-area"></div>
  <div class="abs vline" style="left:185px"></div>
  <div class="abs vline" style="left:487px"></div>
  <div class="abs vline" style="left:713px"></div>

  <h4 class="abs foot-h" style="left:52px;top:915px;font-size:13.5px">Get in Touch</h4>
  <div class="abs social" aria-label="Social links"><span></span><span></span><span></span><span></span></div>

  <h4 class="abs foot-h" style="left:206px;top:915px">Recent Blog</h4>
  <div class="abs blog">
    <p>Lorem ipsum dolor sit amet, consectetuer adipiscing elit. Nam cursus. Morbi ut mi. Nullam enim leo, egestas id, condimentum at, laoreet mattis, massa.</p>
    <p class="by">By Author Name</p>
    <p>Lorem ipsum dolor sit amet, consectetuer adipiscing elit. Nam cursus. Morbi ut mi. Nullam enim leo, egestas id, condimentum at, laoreet mattis, massa.</p>
    <p class="by">By Author Name</p>
  </div>

  <h4 class="abs foot-h" style="left:508px;top:915px">Services List</h4>
  <ul class="abs svc">
    <li><svg width="5" height="8"><path d="M0 0l5 4-5 4z" fill="#999"/></svg>Lorem ipsum , consectetuer adipiscing.</li>
    <li><svg width="5" height="8"><path d="M0 0l5 4-5 4z" fill="#999"/></svg>Morbi ut mi Nullam enim leo</li>
    <li><svg width="5" height="8"><path d="M0 0l5 4-5 4z" fill="#999"/></svg>Egestas id condimentum at</li>
    <li><svg width="5" height="8"><path d="M0 0l5 4-5 4z" fill="#999"/></svg>Laoreet mattis massa.</li>
    <li><svg width="5" height="8"><path d="M0 0l5 4-5 4z" fill="#999"/></svg>Mauris vel lacus vitae felis vestibulum</li>
    <li><svg width="5" height="8"><path d="M0 0l5 4-5 4z" fill="#999"/></svg>Etiam est nunc venenatis in</li>
    <li><svg width="5" height="8"><path d="M0 0l5 4-5 4z" fill="#999"/></svg>Tristique eu imperdiet ac</li>
  </ul>

  <h4 class="abs foot-h" style="left:740px;top:915px">News &amp; Updates</h4>
  <div class="abs news">
    <p>Lorem ipsum , consectetuer adipiscing.<br>Morbi ut mi Nullam enim leo</p>
    <p>Egestas id condimentum at Laoreet mattis<br>massa.</p>
    <p>Mauris vel lacus vitae felis vestibulum<br>Etiam est nunc venenatis</p>
    <p>Donec convallis pede venenatis nibh.</p>
  </div>

  <div class="abs bottom-bar">
    <span class="copy">© 2012 Company Name &nbsp;|&nbsp; All right reserved</span>
    <span class="links">MAIN &nbsp;|&nbsp; ABOUT &nbsp;|&nbsp; SERVICES &nbsp;|&nbsp; PORTFOLIO &nbsp;|&nbsp; SUPPORT &nbsp;|&nbsp; BLOG &nbsp;|&nbsp; CONTACT</span>
  </div>
</footer>
</body>
</html>
```